Mind Ledger - Web Design Project

We need a website for our new company based in Sao Paulo - Brazil. Our initial product is Mind Ledger - an online assessment system based on the most recent neuroscience academic research. The system gathers tests that are applied in the selection and evaluation of employees. We would like to see designs that use the colors black and blue. The final design should communicate trust. We like clean and simple designs.

Login to www.mindledger.com.br
login: user
pass: user

We need three pages:
1- Login page: http://www.mindledger.com.br/

2- Welcome page: http://www.mindledger.com.br/sys/admin/index.php

3- Results page: http://www.mindledger.com.br/sys/admin/admin_provas_resultados.php?unique_id=5

Our logo was created using ArtQuarry.
Next projetcs: Tests interface redesign.

Industry/Entity Type

It Company

Requirements
Must have
• Link folders. i.e.:
Home :: Users :: Paul Wren :: Test1
Nice to have
• Image Buttons
Should not have
• Noise

```html
<!DOCTYPE html>
<html lang="pt-BR">
<head>
<meta charset="utf-8">
<title>Mind Ledger — Home</title>
<link rel="stylesheet" href="https://fonts.googleapis.com/css2?family=Oswald:wght@400;500&family=Arimo:wght@400;700&display=swap">
<style>
  :root {
    --brand-blue: #2070b8;
    --nav-blue: #2a6fb3;
    --ink: #111111;
    --ink-soft: #1e1e1e;
    --paper: #ffffff;
    --paper-shade: #ececec;
    --rule: #d4d4d4;
    --art-light: #3c3c3c;
    --art-dark: #0c0c0c;
  }
  * { box-sizing: border-box; margin: 0; padding: 0; }
  html, body {
    width: 1200px;
    height: 597px;
    overflow: hidden;
    background: var(--paper);
  }
  .page {
    position: relative;
    width: 1200px;
    height: 597px;
    font-family: "Arimo", Arial, sans-serif;
  }

  /* Header */
  .site-header {
    position: absolute;
    top: 0; left: 0;
    width: 1200px;
    height: 56px;
    background: linear-gradient(to bottom, var(--paper) 0%, var(--paper) 55%, var(--paper-shade) 100%);
    border-top: 1px solid var(--rule);
    border-bottom: 1px solid var(--rule);
    z-index: 2;
  }
  .site-header::after {
    content: "";
    position: absolute;
    left: 200px;
    right: 190px;
    bottom: -6px;
    height: 6px;
    border-radius: 50%;
    box-shadow: 0 4px 8px rgba(0, 0, 0, 0.55);
    background: transparent;
  }
  .brand {
    position: absolute;
    left: 188px;
    top: 13px;
    font-family: "Arimo", Arial, sans-serif;
    font-weight: 400;
    font-size: 26px;
    line-height: 30px;
    color: var(--ink-soft);
    text-decoration: none;
    letter-spacing: -0.3px;
  }
  .main-nav {
    position: absolute;
    top: 16px;
    left: 619px;
    display: flex;
    gap: 0;
  }
  .main-nav a {
    font-family: "Oswald", "Arial Narrow", sans-serif;
    font-weight: 500;
    font-size: 18px;
    line-height: 24px;
    color: var(--nav-blue);
    text-decoration: none;
    text-transform: uppercase;
    letter-spacing: 0.2px;
  }
  .main-nav a.is-current { color: var(--ink); }
  .main-nav a:nth-child(1) { margin-right: 22px; }
  .main-nav a:nth-child(2) { margin-right: 22px; }
  .main-nav a:nth-child(3) { margin-right: 23px; }
  .main-nav a:nth-child(4) { margin-right: 23px; }

  /* Hero */
  .hero {
    position: absolute;
    top: 56px; left: 0;
    width: 1200px;
    height: 494px;
    background: var(--brand-blue);
  }
  .hero-art {
    position: absolute;
    left: 170px;
    top: 186px;
    width: 366px;
    height: 308px;
    display: block;
  }
  .hero-copy {
    position: absolute;
    left: 607px;
    top: 234px;
    width: 400px;
  }
  .hero-title {
    font-family: "Oswald", "Arial Narrow", sans-serif;
    font-weight: 500;
    font-size: 41px;
    line-height: 48px;
    text-transform: uppercase;
    letter-spacing: -0.3px;
  }
  .hero-title .line-welcome {
    display: block;
    color: var(--paper);
    text-shadow: 2px 2px 2px rgba(0, 0, 0, 0.55);
  }
  .hero-title .line-name {
    display: block;
    color: var(--ink);
    text-align: right;
    padding-right: 22px;
    text-shadow: 2px 2px 2px rgba(0, 0, 0, 0.35);
  }
  .hero-text {
    margin-top: 12px;
    font-family: "Arimo", Arial, sans-serif;
    font-size: 11px;
    line-height: 19.2px;
    color: var(--paper);
    width: 400px;
  }

  /* Footer */
  .site-footer {
    position: absolute;
    top: 550px; left: 0;
    width: 1200px;
    height: 47px;
    background: linear-gradient(to bottom, var(--paper) 0%, var(--paper) 60%, var(--paper-shade) 100%);
  }
  .copyright {
    position: absolute;
    right: 190px;
    top: 19px;
    font-family: "Arimo", Arial, sans-serif;
    font-weight: 700;
    font-size: 10.5px;
    line-height: 14px;
    color: var(--ink);
  }
</style>
</head>
<body>
<div class="page">
  <header class="site-header">
    <a class="brand" href="http://www.mindledger.com.br/">Mind Ledger</a>
    <nav class="main-nav" aria-label="Principal">
      <a class="is-current" href="http://www.mindledger.com.br/sys/admin/index.php">Home</a>
      <a href="#">Provas</a>
      <a href="#">Usuários</a>
      <a href="#">Configurações</a>
      <a href="#">Logout</a>
    </nav>
  </header>

  <main class="hero">
    <svg class="hero-art" role="img" aria-label="Illustration: silhouette of a human head in profile filled with gears, surrounded by floating cogwheels" viewBox="0 0 366 308">
      <defs>
        <linearGradient id="art-tone" x1="0" y1="0" x2="0" y2="1">
          <stop offset="0" stop-color="#2b6fae"/>
          <stop offset="0.35" stop-color="var(--art-light)"/>
          <stop offset="1" stop-color="var(--art-dark)"/>
        </linearGradient>
      </defs>
      <rect x="0" y="0" width="366" height="308" fill="url(#art-tone)"/>
    </svg>

    <section class="hero-copy">
      <h1 class="hero-title">
        <span class="line-welcome">Bem-vindo ao</span>
        <span class="line-name">Mind Ledger</span>
      </h1>
      <p class="hero-text">Lorem ipsum dolor sit amet, consectetuer adipiscing elit, sed diam nonummy nibh euismod tincidunt ut laoreet dolore magna aliquam erat volutpat. Ut wisi enim ad minim veniam, quis nostrud exerci tation ullamcorper suscipit lobortis nisl ut aliquip ex ea commodo consequat. Duis autem vel eum iriure dolor in hendrerit in vulputate velit esse molestie consequat, vel illum dolore eu feugiat nulla facilisis at vero eros et accumsan et iusto odio dignissim qui blandit praesent luptatum zzril delenit augue duis dolore te feugait nulla facilisi.</p>
    </section>
  </main>

  <footer class="site-footer">
    <p class="copyright">© Copyrights 2013 Mind Ledger. All rights reserved</p>
  </footer>
</div>
</body>
</html>
```